rhyming dictionary website (easy)

i need a web design for my new website which for now runs on my own self made design (i am a programmer so it sucks) you can find it at http://www.lumaquill.com

i would like a nicer design that will not cause visitors to flee in disgust.

Target Market(s)

people who search for rhymes, poets, rappers, and normal birthday greeting people

Requirements
Must have
• this is what it needs to have:

1. main page which is simple and must emphasize on the search bar.

2. search result page that will emphasize on the rhyming words and make them clear and important, it also needs to be separable like in the current "design".
it also need to have a good placement of ads, not too intrusive, not too unnoticeable

3. a general page with no real content that i can fill with anything later.
Nice to have
• also the design could combine the already exist logo that you can see on the website, i added it in the uploaded files, along with its psd.

p.s:
other design i liked that you can inspire yourself from
http://www.zelvoro.com/RhymingDictionary/hello.html

```html
<!DOCTYPE html>
<html lang="en">
<head>
<meta charset="utf-8">
<title>LumaQuill – Design rhymes</title>
<link href="https://fonts.googleapis.com/css2?family=Roboto+Condensed:ital,wght@0,300;0,400;0,700;1,300;1,400&display=swap" rel="stylesheet">
<style>
  :root {
    --header-bg: #ececec;
    --band-top: #4a4a4a;
    --band-bottom: #3e3e3e;
    --band-line: #2a2a2a;
    --ink: #2f2f2f;
    --ink-soft: #3a3a3a;
    --muted: #cfcfcf;
    --link: #5cc6e6;
    --green: #6cc15a;
    --green-dark: #4f9c41;
    --panel: #f4f4f4;
    --row-shade: #e6e6e6;
    --rule: #111;
    --field: #f4f4f4;
    --field-line: #cfcfcf;
    --mark: #3b4fa0;
  }
  * { box-sizing: border-box; margin: 0; padding: 0; }
  html, body { width: 1200px; height: 812px; overflow: hidden; background: #fff; }
  body { font-family: "Roboto Condensed", "Arial Narrow", sans-serif; color: var(--ink); position: relative; }

  .site-header { position: absolute; left: 0; top: 0; width: 1200px; height: 112px; background: var(--header-bg); }
  .brand { position: absolute; left: 189px; top: 38px; display: flex; align-items: center; gap: 18px; }
  .brand-square { width: 62px; height: 30px; display: flex; align-items: center; }
  .brand-square span { display: block; width: 28px; height: 28px; background: var(--mark); }
  .brand-name { font-size: 24px; font-weight: 700; line-height: 1; color: var(--ink); }
  .brand-tagline { font-size: 13px; color: var(--ink); margin-top: 3px; }

  .search { position: absolute; left: 560px; top: 31px; display: flex; gap: 16px; }
  .search-field { width: 333px; height: 49px; border: 1px solid var(--field-line); border-radius: 4px; background: var(--field);
    box-shadow: inset 0 2px 6px rgba(0,0,0,.12); font: italic 400 16px "Roboto Condensed", sans-serif; color: #c4c4c4; padding: 0 19px; line-height: 47px; }
  .search-button { width: 125px; height: 50px; background: var(--green); border-radius: 4px; border-bottom: 4px solid var(--green-dark);
    color: #fff; font-weight: 700; font-size: 16px; text-align: center; line-height: 48px; text-shadow: 0 1px 1px rgba(0,0,0,.35); }

  .latest { position: absolute; left: 0; top: 112px; width: 1200px; height: 92px; border-top: 1px solid var(--band-line);
    background: linear-gradient(var(--band-top), var(--band-bottom)); display: flex; align-items: center; padding-left: 189px; gap: 0; }
  .latest-label { color: #fff; font-weight: 700; font-size: 16px; margin-right: 28px; }
  .latest a { color: var(--link); font-style: italic; font-size: 16px; margin-right: 24px; }

  .result-title { position: absolute; left: 0; top: 232px; width: 1200px; text-align: center; font-size: 46px; font-weight: 700; color: var(--ink); line-height: 1; }
  .result-subtitle { position: absolute; left: 0; top: 307px; width: 1200px; text-align: center; font-size: 23px; color: var(--muted); }

  .rhyme-panel { position: absolute; left: 169px; top: 385px; width: 872px; height: 310px; background: var(--panel); border-radius: 4px; }
  .rhyme-row { position: absolute; left: 18px; width: 826px; height: 56px; display: grid;
    grid-template-columns: 119px 105px 126px 120px 124px 136px auto; align-items: center; padding-left: 7px;
    font-size: 29px; font-weight: 300; font-style: italic; color: var(--ink-soft); border-radius: 4px; }
  .rhyme-row.shaded { background: var(--row-shade); }
  .row-1 { top: 6px; } .row-2 { top: 87px; } .row-3 { top: 152px; } .row-4 { top: 234px; }
  .rhyme-rule { position: absolute; left: 17px; width: 828px; height: 1px; background: var(--rule); }
  .rule-1 { top: 72px; } .rule-2 { top: 156px; } .rule-3 { top: 219px; }

  .site-footer { position: absolute; left: 0; top: 716px; width: 1200px; text-align: center; font-size: 17px; line-height: 28px; color: var(--ink-soft); }
</style>
</head>
<body>
  <header class="site-header">
    <a class="brand" href="http://www.lumaquill.com" style="text-decoration:none">
      <div class="brand-square"><span></span></div>
      <div>
        <div class="brand-name">LumaQuill</div>
        <div class="brand-tagline">- Your online source for rhymes</div>
      </div>
    </a>
    <form class="search">
      <div class="search-field">DESIGN</div>
      <div class="search-button">FIND OUT</div>
    </form>
  </header>

  <nav class="latest">
    <span class="latest-label">LATEST SEARCHES:</span>
    <a href="http://www.zelvoro.com/RhymingDictionary/hello.html">Hello</a>
    <a href="#">Sex</a>
    <a href="#">Dead</a>
    <a href="#">more</a>
    <a href="#">throne</a>
  </nav>

  <main>
    <h1 class="result-title">DESIGN</h1>
    <p class="result-subtitle">One- and two-syllable End Rhymes of design:</p>

    <section class="rhyme-panel">
      <div class="rhyme-row row-1"><span>airline</span><span>align</span><span>assign</span><span>define</span><span>divine</span><span>deadline</span><span>highline</span></div>
      <div class="rhyme-rule rule-1"></div>
      <div class="rhyme-row row-2 shaded"><span>airline</span><span>align</span><span>assign</span><span>define</span><span>divine</span><span>deadline</span><span>highline</span></div>
      <div class="rhyme-rule rule-2"></div>
      <div class="rhyme-row row-3"><span>airline</span><span>align</span><span>assign</span><span>define</span><span>divine</span><span>deadline</span><span>highline</span></div>
      <div class="rhyme-rule rule-3"></div>
      <div class="rhyme-row row-4 shaded"><span>airline</span><span>align</span><span>assign</span><span>define</span><span>divine</span><span>deadline</span><span>highline</span></div>
    </section>
  </main>

  <footer class="site-footer">
    <p>All rights are allright</p>
    <p>They are reserved as they well deserved.</p>
  </footer>
</body>
</html>
```